Business Cards for 41Vale

I need business cards that goes with the logo
Updates

Dear designers - many thanks for the responsesreceived to date. There are many good designs but most of them are landscape.Could you please submit a few options for portrait layout as well.

Industry/Entity Type

Business

```html
<!DOCTYPE html>
<html lang="en">
<head>
<meta charset="UTF-8">
<title>41Vale Business Cards</title>
<link rel="stylesheet" href="https://fonts.googleapis.com/css2?family=Titillium+Web:wght@400;700&display=swap">
<style>
  :root {
    --backdrop: #e4e4e4;
    --card: #ffffff;
    --brand-red: #e31e26;
    --brand-slate: #434a50;
    --ink: #2e3236;
    --on-dark: #ffffff;
  }
  * { margin: 0; padding: 0; box-sizing: border-box; }
  html, body {
    width: 1200px;
    height: 1200px;
    overflow: hidden;
    background: var(--backdrop);
    font-family: "Titillium Web", sans-serif;
  }
  .canvas { position: relative; width: 1200px; height: 1200px; }

  .card {
    position: absolute;
    left: 185px;
    width: 830px;
    height: 460px;
    background: var(--card);
    overflow: hidden;
  }
  .card-front { top: 98px; }
  .card-back { top: 640px; }

  .brand {
    position: absolute;
    display: flex;
    align-items: center;
    gap: 14px;
    font-weight: 700;
    color: var(--brand-slate);
    line-height: 1;
  }
  .brand-dot {
    border-radius: 50%;
    background: var(--brand-red);
    flex: none;
  }
  .card-front .brand {
    left: 50%;
    top: 50%;
    transform: translate(-50%, -50%);
    font-size: 96px;
  }
  .card-front .brand-dot { width: 44px; height: 44px; }

  .card-back .top-band {
    position: absolute;
    left: 0; top: 0;
    width: 100%;
    height: 27px;
    background: var(--brand-red);
  }
  .card-back .bottom-band {
    position: absolute;
    left: 0; bottom: 0;
    width: 100%;
    height: 82px;
    background: var(--brand-slate);
  }
  .card-back .website {
    position: absolute;
    left: 137px;
    top: 50%;
    transform: translateY(-50%);
    color: var(--on-dark);
    font-size: 22px;
    font-weight: 700;
  }
  .card-back .brand {
    left: 100px;
    top: 178px;
    font-size: 66px;
  }
  .card-back .brand-dot { width: 30px; height: 30px; }

  .contact {
    position: absolute;
    left: 498px;
    top: 64px;
    color: var(--ink);
  }
  .contact .name {
    font-size: 30px;
    font-weight: 700;
    line-height: 1.05;
  }
  .contact .role {
    font-size: 24px;
    color: var(--brand-red);
    line-height: 1.1;
  }
  .contact .address {
    margin-top: 78px;
    font-size: 22px;
    line-height: 1.35;
  }
  .contact .reach {
    margin-top: 30px;
    font-size: 22px;
    line-height: 1.35;
  }
</style>
</head>
<body>
<main class="canvas">
  <section class="card card-front" aria-label="Card front">
    <div class="brand"><span class="brand-dot"></span><span class="brand-name">41Vale</span></div>
  </section>

  <section class="card card-back" aria-label="Card back">
    <div class="top-band"></div>
    <div class="brand"><span class="brand-dot"></span><span class="brand-name">41Vale</span></div>
    <div class="contact">
      <p class="name">Martin Holloway</p>
      <p class="role">manager</p>
      <p class="address">City, State Name<br>31 StreetName str.</p>
      <p class="reach">555-014-2380<br>name@domain.com</p>
    </div>
    <div class="bottom-band">
      <p class="website">www.domain.com</p>
    </div>
  </section>
</main>
</body>
</html>
```